Stylish Business Cards Wanted

- DOUBLE SIDED Design Required -

High end, edgy cards for a corporate and personal stylist. Must include logo,
Name: Belinda Marsh
Title: Director and Stylist
telephone : +61 8 8417 2950
email: belinda@thewardrobeledger.com
website: thewardrobeledger.com
Tag: Corporate Workwear & Uniform Specialist | Personal Stylist
Would like nice icons for telephone, email, website

Target Market(s)

Businesses wanting stylish uniforms, people wanting stylish wardrobes

Industry/Entity Type

Corporate Workwear Stylist

Contact Information for Business Card

I would like black, white and gold foiling incorporated in the design - possibly a touch of the other colours on my branding guide attached Name: Belinda Marsh Title: Director and Stylist telephone : +61 8 8417 2950 email: belinda@thewardrobeledger.com website: thewardrobeledger.com Tag: Corporate Workwear & Uniform Specialist | Personal Stylist Would like nice icons for telephone, email, website

Font styles to use
Other font styles liked:
• Raleway

Colors

Designer to choose colors to be used in the design.

Requirements
Must have
• Gold foil accents

```html
<!DOCTYPE html>
<html lang="en">
<head>
<meta charset="utf-8">
<title>The Wardrobe Ledger – Business Cards</title>
<link rel="stylesheet" href="https://fonts.googleapis.com/css2?family=Lato:wght@400;700&display=swap">
<style>
  :root {
    --backdrop: #2a2a2b;
    --card: #1c1d1f;
    --pattern: #18191b;
    --ink-light: #e6e7e6;
    --ink-soft: #c9cac9;
    --gold: #e0b43f;
    --rule: #6c6d6e;
  }
  * { box-sizing: border-box; margin: 0; padding: 0; }
  html, body { width: 1200px; height: 1108px; overflow: hidden; }
  body {
    background: var(--backdrop);
    font-family: "Lato", Arial, sans-serif;
    position: relative;
  }
  .card {
    position: absolute;
    top: 204px;
    width: 400px;
    height: 700px;
    background: var(--card);
    border-radius: 24px;
    box-shadow: 0 18px 40px rgba(0,0,0,.45);
    overflow: hidden;
  }
  .card--front { left: 160px; }
  .card--back { left: 640px; }

  .brand-name {
    color: var(--ink-light);
    font-weight: 700;
    text-align: center;
    letter-spacing: 1px;
    line-height: 1.15;
  }
  .card--front .brand-name {
    position: absolute;
    top: 160px; left: 0; right: 0;
    font-size: 40px;
  }

  .holder {
    position: absolute;
    top: 440px; left: 0; right: 0;
    text-align: center;
  }
  .holder__name {
    color: var(--ink-light);
    font-weight: 700;
    font-size: 30px;
    letter-spacing: 1px;
    text-transform: uppercase;
  }
  .holder__title {
    color: var(--gold);
    font-size: 17px;
    letter-spacing: .5px;
    text-transform: uppercase;
    margin-top: 4px;
  }
  .contact-icons {
    display: flex;
    align-items: center;
    justify-content: center;
    gap: 8px;
    margin: 22px auto 0;
    width: 280px;
  }
  .contact-icons .rule {
    flex: 1;
    height: 1px;
    background: var(--rule);
  }
  .contact-icons svg { width: 34px; height: 34px; display: block; }
  .contact-list {
    list-style: none;
    margin-top: 14px;
    color: var(--ink-soft);
    font-size: 18px;
    line-height: 1.4;
  }

  .back-pattern {
    position: absolute;
    inset: 0;
    background: linear-gradient(160deg, #1e1f21 0%, var(--pattern) 60%, #1d1e20 100%);
  }
  .card--back .brand-name {
    position: absolute;
    top: 300px; left: 0; right: 0;
    font-size: 30px;
  }
  .tagline {
    position: absolute;
    bottom: 70px; left: 0; right: 0;
    text-align: center;
    color: #f2f2f2;
    font-size: 17px;
    line-height: 1.4;
  }
</style>
</head>
<body>

<section class="card card--front" aria-label="Card front">
  <h1 class="brand-name">The Wardrobe<br>Ledger</h1>

  <div class="holder">
    <p class="holder__name">Belinda Marsh</p>
    <p class="holder__title">Director and Stylist</p>

    <div class="contact-icons">
      <span class="rule"></span>
      <svg viewBox="0 0 34 34" aria-label="Telephone" role="img">
        <rect width="34" height="34" rx="4" fill="var(--gold)"/>
        <path d="M9 13c0-3 4-4 8-4s8 1 8 4v2h-4v-2h-8v2H9z" fill="var(--card)"/>
        <path d="M11 16h12l2 9H9z" fill="var(--card)"/>
        <circle cx="17" cy="20.5" r="2.2" fill="var(--gold)"/>
      </svg>
      <svg viewBox="0 0 34 34" aria-label="Email" role="img">
        <rect width="34" height="34" rx="4" fill="var(--gold)"/>
        <rect x="7" y="10" width="20" height="14" fill="none" stroke="var(--card)" stroke-width="2"/>
        <path d="M7 10l10 8 10-8M7 24l7-7M27 24l-7-7" fill="none" stroke="var(--card)" stroke-width="2"/>
      </svg>
      <svg viewBox="0 0 34 34" aria-label="Website" role="img">
        <rect width="34" height="34" rx="4" fill="var(--gold)"/>
        <circle cx="17" cy="17" r="9" fill="none" stroke="var(--card)" stroke-width="2"/>
        <ellipse cx="17" cy="17" rx="4" ry="9" fill="none" stroke="var(--card)" stroke-width="1.6"/>
        <path d="M8 17h18" stroke="var(--card)" stroke-width="1.6"/>
      </svg>
      <span class="rule"></span>
    </div>

    <ul class="contact-list">
      <li>+61 8 8417 2950</li>
      <li>belinda@thewardrobeledger.com</li>
      <li>thewardrobeledger.com</li>
    </ul>
  </div>
</section>

<section class="card card--back" aria-label="Card back">
  <div class="back-pattern" role="img" aria-label="Faint repeating brand pattern in spot gloss"></div>
  <p class="brand-name">The Wardrobe<br>Ledger</p>
  <p class="tagline">Corporate Workwear &amp; Uniform Specialist<br>Personal Stylist</p>
</section>

</body>
</html>
```